Stationery Design Project

I am a personal trainer in the fitness industry based in Miami. I have recently designed a logo for my company, now i need to market my name through selected stationery designs.
I need an email signature, invoice and a business card. I am looking for a design that is fresh and eye catching to my target audience.
Updates

Reason: Waiting for photo to be taken for business card.

Target Market(s)

25 to 65 years old - male and female - overweight, sedentary and athletic clientele - middle to wealthy economic class

Industry/Entity Type

Personal Trainer

Requirements
Must have
• Will attach Zip file with logo, template of invoice and personal information.
Will attach photo for business card in the next few days.
Nice to have
• Black backdrop logo image for banner of Invoice, with transparent images of my logo.
White backdrop logo image for Email signature, with font that works well with logo.

```html
<!DOCTYPE html>
<html lang="en">
<head>
<meta charset="utf-8">
<title>Pulse Motion Studio – Business Card</title>
<link rel="stylesheet" href="https://fonts.googleapis.com/css2?family=Open+Sans:wght@400;600;700&display=swap">
<style>
  :root {
    --backdrop: #141414;
    --orange: #ef5a24;
    --orange-deep: #e9462a;
    --amber: #f6a01e;
    --yellow: #f5e11d;
    --white: #ffffff;
    --ink: #3a3a3a;
    --rule: #9a9a9a;
    --grey: #6b6b6b;
  }
  * { margin: 0; padding: 0; box-sizing: border-box; }
  html, body { width: 1200px; height: 943px; overflow: hidden; background: var(--backdrop); }
  body { font-family: "Open Sans", Arial, sans-serif; position: relative; }

  .card { position: absolute; overflow: hidden; box-shadow: 0 18px 40px rgba(0,0,0,.6); }

  /* Front of card */
  .card-front {
    left: 590px; top: 70px; width: 540px; height: 309px;
    background: radial-gradient(ellipse 55% 60% at 50% 48%, var(--yellow) 0%, var(--amber) 45%, var(--orange-deep) 100%);
    display: flex; align-items: center; justify-content: center; gap: 14px;
  }
  .card-front .brand-dot { width: 34px; height: 34px; border-radius: 50%; background: var(--white); }
  .card-front .brand-name { font-weight: 700; font-size: 36px; color: var(--white); letter-spacing: 1px; text-transform: uppercase; }

  /* Back of card */
  .card-back {
    left: 90px; top: 410px; width: 640px; height: 366px;
    background: var(--white);
  }
  .back-brand { position: absolute; left: 38px; top: 34px; display: flex; align-items: center; gap: 14px; }
  .back-brand .brand-dot { width: 38px; height: 38px; border-radius: 50%; background: var(--orange); }
  .back-brand .brand-name { font-weight: 700; font-size: 30px; color: var(--orange); text-transform: uppercase; letter-spacing: 1px; }

  .contact { position: absolute; left: 38px; top: 118px; width: 400px; color: var(--ink); font-size: 13px; }
  .contact .person { font-size: 14px; padding-bottom: 6px; border-bottom: 1px solid var(--rule); }
  .contact .person-name { color: var(--orange); font-weight: 600; font-size: 19px; }
  .contact .address { padding-top: 8px; }
  .contact .lines { padding: 4px 0 8px; border-bottom: 1px solid var(--rule); display: flex; gap: 12px; align-items: center; }
  .contact .lines span { display: inline-flex; align-items: center; gap: 4px; }
  .contact svg { width: 12px; height: 12px; fill: var(--orange); }
  .contact .web { padding-top: 10px; font-size: 14px; }
  .contact .web b { color: var(--orange); font-size: 19px; font-weight: 600; letter-spacing: 1px; }

  .accent-band {
    position: absolute; left: 0; bottom: 0; width: 380px; height: 16px;
    background: linear-gradient(90deg, var(--orange-deep), var(--amber) 60%, var(--yellow));
  }
  .accent-circle {
    position: absolute; right: -90px; bottom: -110px; width: 300px; height: 300px; border-radius: 50%;
    background: linear-gradient(160deg, var(--yellow), var(--amber) 40%, var(--orange-deep));
  }

  /* Standalone wordmark */
  .wordmark { position: absolute; left: 70px; top: 800px; display: flex; align-items: center; gap: 12px; }
  .wordmark .brand-dot { width: 28px; height: 28px; border-radius: 50%; background: var(--white); }
  .wordmark .brand-name { font-weight: 700; font-size: 28px; color: var(--white); text-transform: uppercase; letter-spacing: 1px; }
</style>
</head>
<body>

  <section class="card card-front">
    <span class="brand-dot"></span>
    <span class="brand-name">Pulse Motion Studio</span>
  </section>

  <section class="card card-back">
    <div class="back-brand">
      <span class="brand-dot"></span>
      <span class="brand-name">Pulse Motion Studio</span>
    </div>

    <div class="contact">
      <p class="person"><span class="person-name">Dana Reyes</span> | Personal Fitness Trainer</p>
      <p class="address">48 Harbor Lane, Suite 310, Miami, FL 33130</p>
      <p class="lines">
        <span><svg viewBox="0 0 24 24"><path d="M6.6 10.8a15 15 0 0 0 6.6 6.6l2.2-2.2a1 1 0 0 1 1-.25 11.4 11.4 0 0 0 3.6.57 1 1 0 0 1 1 1V20a1 1 0 0 1-1 1A17 17 0 0 1 3 4a1 1 0 0 1 1-1h3.5a1 1 0 0 1 1 1c0 1.25.2 2.45.57 3.57a1 1 0 0 1-.25 1z"/></svg>305-555-0147</span>
        <span><svg viewBox="0 0 24 24"><rect x="6" y="1" width="12" height="22" rx="2"/></svg>305-555-0192</span>
        <span><b style="color:var(--orange)">@</b>hello@pulsemotionstudio.com</span>
      </p>
      <p class="web">www.<b>pulsemotionstudio</b>.com</p>
    </div>

    <div class="accent-band"></div>
    <div class="accent-circle"></div>
  </section>

  <div class="wordmark">
    <span class="brand-dot"></span>
    <span class="brand-name">Pulse Motion Studio</span>
  </div>

</body>
</html>
```